Independent Financial Advisor Billboard Campaign - Granite Bridge Financial

I am a local, independent financial advisor. My company is Granite Bridge Financial, located in Charleston, WV. My main source of revenue comes from those nearing or entering retirement that need assistance with financial planning and investment management. Many are looking to rollover their employer retirement plan into an IRA account. I would like a billboard design campaign that focuses on this type of client. Please see our website www.granitebridgefinancial-example.com for more information.

```html
<!DOCTYPE html>
<html lang="en">
<head>
<meta charset="utf-8">
<title>Granite Bridge Financial – Retirement Done Right</title>
<link href="https://fonts.googleapis.com/css2?family=Roboto:wght@400;500;700;900&display=swap" rel="stylesheet">
<style>
  :root {
    --navy: #17427a;
    --navy-dark: #0f3262;
    --grey: #6b6b6b;
    --grey-light: #8a8a8a;
    --white: #ffffff;
    --ink: #333a44;
    --page: #eef1f5;
  }
  * { box-sizing: border-box; margin: 0; padding: 0; }
  html, body { width: 1200px; height: 871px; overflow: hidden; background: var(--page); }
  body { font-family: "Roboto", Arial, sans-serif; position: relative; }

  .billboard {
    position: absolute; left: 40px; top: 265px;
    width: 1120px; height: 340px;
    background: var(--white);
    overflow: hidden;
    box-shadow: 0 6px 24px rgba(20, 40, 80, .18);
  }
  .billboard__shapes { position: absolute; inset: 0; }

  .brand {
    position: absolute; left: 30px; top: 40px;
    display: flex; align-items: center; gap: 12px;
  }
  .brand__mark { width: 34px; height: 34px; background: var(--navy); }
  .brand__name {
    font-weight: 700; font-size: 22px; color: var(--navy);
    letter-spacing: .5px; line-height: 1.05; width: 190px;
  }

  .address {
    position: absolute; left: 470px; top: 18px;
    display: flex; align-items: center; gap: 12px;
    color: var(--ink); font-size: 19px; font-weight: 500; line-height: 1.2;
  }
  .address svg { width: 28px; height: 38px; }

  .advisor-photo {
    position: absolute; left: 30px; top: 115px;
    width: 128px; height: 126px;
    border: 4px solid var(--white);
    background: linear-gradient(160deg, #a8745a 0%, #8c6450 45%, #2c3b5c 100%);
  }

  .headline {
    position: absolute; left: 192px; top: 130px;
    color: var(--white); text-transform: uppercase;
  }
  .headline__lead { font-size: 33px; font-weight: 500; letter-spacing: .5px; line-height: 1; }
  .headline__main { font-size: 72px; font-weight: 900; line-height: 1; margin-top: 4px; }

  .cta {
    position: absolute; left: 22px; top: 250px;
    color: var(--white); font-size: 42px; font-weight: 700; letter-spacing: 1px;
  }

  .contact {
    position: absolute; top: 302px;
    display: flex; align-items: center; gap: 9px;
    color: var(--ink); font-size: 14px; white-space: nowrap;
  }
  .contact--email { left: 26px; }
  .contact--web { left: 352px; }
  .contact__icon {
    width: 26px; height: 26px; border-radius: 4px; background: var(--navy);
    display: flex; align-items: center; justify-content: center;
  }
  .contact__icon svg { width: 17px; height: 17px; }

  .clients-photo { position: absolute; inset: 0; }
</style>
</head>
<body>
  <section class="billboard">
    <svg class="billboard__shapes" viewBox="0 0 1120 340" width="1120" height="340">
      <polygon points="340,0 372,0 452,92 422,92" fill="var(--navy)"/>
      <polygon points="372,0 400,0 462,78 700,68 712,96 452,92" fill="var(--grey)"/>
      <rect x="0" y="108" width="700" height="132" fill="var(--navy)"/>
      <rect x="172" y="108" width="6" height="132" fill="var(--white)"/>
      <polygon points="0,248 690,232 680,290 0,300" fill="var(--grey)"/>
      <path d="M760,0 Q670,150 705,340" fill="none" stroke="var(--grey-light)" stroke-width="8"/>
      <path d="M790,0 Q700,160 735,340" fill="none" stroke="var(--navy)" stroke-width="26"/>
    </svg>

    <svg class="clients-photo" viewBox="0 0 1120 340" width="1120" height="340" role="img" aria-label="Photo of a smiling retired couple embracing at home">
      <defs>
        <linearGradient id="couple-tones" x1="0" y1="0" x2="1" y2="1">
          <stop offset="0" stop-color="#e6d3c4"/>
          <stop offset=".5" stop-color="#c9a996"/>
          <stop offset="1" stop-color="#3d4f66"/>
        </linearGradient>
      </defs>
      <path d="M805,0 L1120,0 L1120,340 L750,340 Q718,160 805,0 Z" fill="url(#couple-tones)"/>
    </svg>

    <div class="brand">
      <span class="brand__mark"></span>
      <span class="brand__name">GRANITE BRIDGE FINANCIAL</span>
    </div>

    <div class="address">
      <svg viewBox="0 0 28 38" aria-hidden="true">
        <path d="M14 2a10 10 0 0 0-10 10c0 8 10 18 10 18s10-10 10-18A10 10 0 0 0 14 2z" fill="var(--navy)"/>
        <circle cx="14" cy="12" r="4" fill="var(--white)"/>
        <ellipse cx="14" cy="34" rx="11" ry="3" fill="none" stroke="var(--navy)" stroke-width="2"/>
      </svg>
      <p>48 Summit Lane<br>Charleston, WV 25301</p>
    </div>

    <div class="advisor-photo" role="img" aria-label="Portrait of the financial advisor in a navy suit"></div>

    <h1 class="headline">
      <span class="headline__lead">Retirement</span><br>
      <span class="headline__main">Done Right</span>
    </h1>

    <p class="cta">CALL NOW : 304.555.0148</p>

    <p class="contact contact--email">
      <span class="contact__icon">
        <svg viewBox="0 0 18 18" aria-hidden="true"><rect x="2" y="4" width="14" height="10" fill="none" stroke="#fff" stroke-width="1.6"/><path d="M2 4l7 6 7-6" fill="none" stroke="#fff" stroke-width="1.6"/></svg>
      </span>
      alex@granitebridgefinancial-example.com
    </p>
    <p class="contact contact--web">
      <span class="contact__icon">
        <svg viewBox="0 0 18 18" aria-hidden="true"><circle cx="9" cy="9" r="7" fill="none" stroke="#fff" stroke-width="1.4"/><ellipse cx="9" cy="9" rx="3" ry="7" fill="none" stroke="#fff" stroke-width="1.2"/><path d="M2 9h14M3.5 5.5h11M3.5 12.5h11" stroke="#fff" stroke-width="1.1"/></svg>
      </span>
      www.granitebridgefinancial-example.com
    </p>
  </section>
</body>
</html>
```